Need small adjustment to BT organics logo. Have a design to go off.
Then i need the label design completed. i have attached the file as a reference.

Logo Text

Bright Tide Organics

Colors

Designer to choose colors to be used in the design.

Requirements
Must have
• Info in file attched. Plus the small CBD logos
Should not have
• Remove Bright Tide Kitchen Appliances under sample design

```html
<!DOCTYPE html>
<html lang="en">
<head>
<meta charset="utf-8">
<title>Bright Tide Organics – Platinum Broad Spectrum CBD Oil Label</title>
<link href="https://fonts.googleapis.com/css2?family=Montserrat:wght@400;500&family=Oswald:wght@300;400&family=Parisienne&family=Libre+Franklin:wght@400;700;900&display=swap" rel="stylesheet">
<style>
  :root{
    --bg:#e4e4e4;
    --paper:#ffffff;
    --green:#8cc63f;
    --teal:#3cbfc0;
    --blue:#2a7fc0;
    --lavender:#b7a3d9;
    --lavender-soft:#e6ddf3;
    --grey:#6d6e71;
    --grey-dark:#58595b;
    --ink:#231f20;
    --script:#8a9a7a;
  }
  *{box-sizing:border-box;margin:0;padding:0}
  html,body{width:1200px;height:800px;overflow:hidden}
  body{background:var(--bg);position:relative;font-family:"Montserrat",sans-serif}

  .label{position:absolute;left:50px;top:162px;width:1100px;height:476px;background:var(--paper);overflow:hidden}
  .label__top-rule{position:absolute;left:0;top:0;width:100%;height:7px;background:linear-gradient(90deg,var(--green),var(--teal) 55%,var(--blue))}
  .label__bottom-band{position:absolute;left:0;bottom:0;width:100%;height:31px;background:linear-gradient(90deg,var(--green) 0%,var(--teal) 22%,var(--blue) 35%,var(--blue) 65%,var(--teal) 80%,var(--green) 100%)}
  .label__volume{position:absolute;left:387px;bottom:0;width:325px;height:31px;background:var(--grey);color:#fff;font-size:14px;letter-spacing:.5px;display:flex;align-items:center;justify-content:center}

  .decor{position:absolute}
  .decor--leaf-sprig{left:472px;top:7px;width:118px;height:52px;background:radial-gradient(ellipse at center,rgba(140,198,63,.45),rgba(140,198,63,0) 70%)}
  .decor--hemp-right{left:740px;top:150px;width:260px;height:290px;background:radial-gradient(ellipse at center,rgba(109,110,113,.10),rgba(109,110,113,0) 68%)}
  .decor--hemp-left{left:150px;top:80px;width:260px;height:300px;background:radial-gradient(ellipse at center,rgba(140,198,63,.14),rgba(140,198,63,0) 68%)}
  .decor--wash{left:420px;top:290px;width:270px;height:150px;background:radial-gradient(ellipse at center,rgba(180,214,120,.22),rgba(180,214,120,0) 70%)}

  /* Nutrition panel */
  .nutrition{position:absolute;left:53px;top:66px;width:199px;height:356px;border:1px solid var(--ink);padding:3px 5px;font-family:"Libre Franklin",sans-serif;color:var(--ink);font-size:7.6px;line-height:1.25}
  .nutrition__title{font-weight:900;font-size:22px;line-height:1;letter-spacing:-.3px}
  .nutrition__servings{font-size:8.5px}
  .nutrition__size{display:flex;justify-content:space-between;font-weight:900;font-size:10px;border-bottom:7px solid var(--ink);padding-bottom:2px}
  .nutrition__amount{font-weight:700;font-size:6.5px;padding-top:2px}
  .nutrition__calories{display:flex;justify-content:space-between;align-items:flex-end;font-weight:900;font-size:16px;line-height:1;border-bottom:4px solid var(--ink);padding-bottom:2px}
  .nutrition__calories span:last-child{font-size:22px}
  .nutrition__dv{text-align:right;font-weight:700;font-size:6.5px;border-bottom:1px solid var(--ink);padding:1px 0}
  .nutrition__row{display:flex;justify-content:space-between;border-bottom:1px solid var(--ink);padding:1.6px 0}
  .nutrition__row b{font-weight:700}
  .nutrition__row--indent{padding-left:9px}
  .nutrition__row--indent2{padding-left:18px}
  .nutrition__row--thick{border-bottom:7px solid var(--ink)}
  .nutrition__row--last{border-bottom:4px solid var(--ink)}
  .nutrition__warning{font-size:5px;line-height:1.25;padding-top:2px}

  /* Brand block */
  .brand{position:absolute;left:380px;top:128px;width:335px;display:flex;align-items:center;justify-content:center;gap:10px}
  .brand__dot{width:18px;height:18px;border-radius:50%;background:var(--teal);flex:none}
  .brand__name{font-weight:400;font-size:23px;letter-spacing:1.2px;color:var(--grey-dark);text-transform:uppercase;white-space:nowrap}

  .variant{position:absolute;left:380px;top:207px;width:335px;height:30px;background:linear-gradient(90deg,rgba(183,163,217,.15),var(--lavender-soft) 30%,var(--lavender-soft) 70%,rgba(183,163,217,.15));text-align:center;font-family:"Parisienne",cursive;font-size:28px;line-height:32px;color:var(--lavender)}
  .product-type{position:absolute;left:360px;top:243px;width:375px;text-align:center;font-family:"Parisienne",cursive;font-size:24px;color:var(--script)}

  /* Claims grid */
  .claims{position:absolute;left:380px;top:290px;width:335px;display:grid;grid-template-columns:repeat(3,1fr);row-gap:4px;list-style:none}
  .claim{display:flex;flex-direction:column;align-items:center;gap:3px;height:44px}
  .claim svg{width:21px;height:21px;stroke:var(--green);fill:none;stroke-width:1.6;stroke-linecap:round;stroke-linejoin:round}
  .claim__label{font-size:9.5px;color:var(--green);letter-spacing:.2px;white-space:nowrap}

  /* Product info */
  .info{position:absolute;right:47px;top:30px;width:260px;text-align:right;font-family:"Oswald",sans-serif;font-weight:300;font-size:14px;line-height:24.5px;color:var(--ink);text-transform:uppercase}
  .info__block + .info__block{margin-top:8px}
</style>
</head>
<body>
<main class="label">
  <div class="label__top-rule"></div>

  <div class="decor decor--hemp-left" role="img" aria-label="Faint watercolour leaf decoration"></div>
  <div class="decor decor--hemp-right" role="img" aria-label="Faint outlined hemp leaf decoration"></div>
  <div class="decor decor--leaf-sprig" role="img" aria-label="Green watercolour leaf sprig"></div>
  <div class="decor decor--wash" role="img" aria-label="Soft green watercolour wash behind the claims"></div>

  <section class="nutrition" aria-label="Nutrition Facts">
    <div class="nutrition__title">Nutrition Facts</div>
    <div class="nutrition__servings">4 servings per container</div>
    <div class="nutrition__size"><span>Serving size</span><span>1 cup (180g)</span></div>
    <div class="nutrition__amount">Amount per serving</div>
    <div class="nutrition__calories"><span>Calories</span><span>245</span></div>
    <div class="nutrition__dv">% Daily Value*</div>
    <div class="nutrition__row"><span><b>Total Fat</b> 12g</span><b>14%</b></div>
    <div class="nutrition__row nutrition__row--indent"><span>Saturated Fat 2g</span><b>10%</b></div>
    <div class="nutrition__row nutrition__row--indent"><span>Trans Fat 0g</span><span></span></div>
    <div class="nutrition__row"><span><b>Cholesterol</b> 8mg</span><b>3%</b></div>
    <div class="nutrition__row"><span><b>Sodium</b> 210mg</span><b>9%</b></div>
    <div class="nutrition__row"><span><b>Total Carbohydrate</b> 34g</span><b>12%</b></div>
    <div class="nutrition__row nutrition__row--indent"><span>Dietary Fiber 7g</span><b>25%</b></div>
    <div class="nutrition__row nutrition__row--indent"><span>Total Sugars 5g</span><span></span></div>
    <div class="nutrition__row nutrition__row--indent2"><span>Includes 4g Added Sugars</span><b>8%</b></div>
    <div class="nutrition__row nutrition__row--thick"><span><b>Protein</b> 11g</span><span></span></div>
    <div class="nutrition__row"><span>Vitamin D 4mcg</span><span>20%</span></div>
    <div class="nutrition__row"><span>Calcium 210mg</span><span>16%</span></div>
    <div class="nutrition__row"><span>Iron 4mg</span><span>22%</span></div>
    <div class="nutrition__row nutrition__row--last"><span>Potassium 380mg</span><span>8%</span></div>
    <p class="nutrition__warning"><b>WARNING:</b> CONSULT WITH YOUR HEALTHCARE PROVIDER BEFORE USING IF YOU ARE NURSING, PREGNANT OR TAKING MEDICATION. IF ADVERSE REACTION OCCURS, DISCONTINUE USE.</p>
  </section>

  <div class="brand">
    <span class="brand__dot"></span>
    <span class="brand__name">Bright Tide Organics</span>
  </div>

  <div class="variant">Platinum</div>
  <div class="product-type">Broad Spectrum CBD Oil</div>

  <ul class="claims">
    <li class="claim"><svg viewBox="0 0 24 24"><path d="M12 21V11M12 11C9 8 9 4 12 2c3 2 3 6 0 9zM12 13c-3-2-7-2-9 0 2 2 6 2 9 0zM12 13c3-2 7-2 9 0-2 2-6 2-9 0z"/></svg><span class="claim__label">THC FREE</span></li>
    <li class="claim"><svg viewBox="0 0 24 24"><path d="M12 22V12M12 12C12 7 8 4 3 4c0 5 4 8 9 8zM12 14c0-4 3-7 8-7 0 4-3 7-8 7z"/></svg><span class="claim__label">100% NATURAL</span></li>
    <li class="claim"><svg viewBox="0 0 24 24"><path d="M4 11l6 9L21 3M9 13c0-4 2-7 6-8"/></svg><span class="claim__label">NON GMO</span></li>
    <li class="claim"><svg viewBox="0 0 24 24"><path d="M12 3C9 8 6 11 6 15a6 6 0 0 0 12 0c0-4-3-7-6-12z"/></svg><span class="claim__label">100% PURE</span></li>
    <li class="claim"><svg viewBox="0 0 24 24"><circle cx="12" cy="12" r="9"/><path d="M8 12l3 3 5-6"/></svg><span class="claim__label">GMP CERTIFIED</span></li>
    <li class="claim"><svg viewBox="0 0 24 24"><path d="M9 3h6M10 3v6l-5 10a2 2 0 0 0 2 2h10a2 2 0 0 0 2-2l-5-10V3M7 15h10"/></svg><span class="claim__label">LAB TESTED</span></li>
    <li class="claim"><svg viewBox="0 0 24 24"><path d="M6 8l1 2 2 .3-1.5 1.4.4 2.1L6 12.8l-1.9 1 .4-2.1L3 10.3 5 10zM12 8l1 2 2 .3-1.5 1.4.4 2.1-1.9-1-1.9 1 .4-2.1L9 10.3 11 10zM18 8l1 2 2 .3-1.5 1.4.4 2.1-1.9-1-1.9 1 .4-2.1-1.5-1.4 2-.3zM3 18h18"/></svg><span class="claim__label">MADE IN USA</span></li>
    <li class="claim"><svg viewBox="0 0 24 24"><circle cx="12" cy="12" r="9"/><path d="M6 6l12 12M12 7v3M10 9h4"/></svg><span class="claim__label">NO PESTICIDES</span></li>
    <li class="claim"><svg viewBox="0 0 24 24"><path d="M12 6c-2 3-2 7 0 10 2-3 2-7 0-10zM12 16c-3-1-6-4-6-8 3 1 5 4 6 8zM12 16c3-1 6-4 6-8-3 1-5 4-6 8zM3 18h18"/></svg><span class="claim__label">INDUSTRIAL HEMP</span></li>
  </ul>

  <section class="info">
    <div class="info__block">
      <p>Serving size:1</p>
      <p>Dropper(1ml)</p>
      <p>CBD per serving:20mg</p>
      <p>Serving per bottle: 30</p>
    </div>
    <div class="info__block">
      <p>Ingredients:</p>
      <p>Organically grown</p>
      <p>Vitasorba* optimized broad</p>
      <p>spectrum CBD hemp oil,</p>
      <p>Vitasorb* melatonin, MCT oil,</p>
      <p>natural flavours, stvia.</p>
    </div>
    <div class="info__block">
      <p>Suggested use*</p>
      <p>Shake well, fill</p>
      <p>dropper and place</p>
      <p>under tongue. Store</p>
      <p>away from heat, light</p>
      <p>and humidity.</p>
    </div>
  </section>

  <div class="label__bottom-band"></div>
  <div class="label__volume">30ml 1000mg</div>
</main>
</body>
</html>
```